New River III Precinct 6x11 GOTV postcard

We require BOTH persuasive copy and high-impact layout for an oversized 6x11 political mailer. This might be one person, but it likely requires a specialized "creative team." of an experienced political strategist copywriter PLUS a graphic designer - so the words fit the exact layout block, and the visuals reinforce the psychological punch of the headline.

The goal is to remove all excuses a targeted audience of ~900 registered Harvestline + ~1800 Unaffiliated voters in our precinct - have for not voting.

I need to be able to work by phone / online chat to iterate designs
I need to own the design in the top couple of software outputs that any printer service will require.

I want to experiment with very subtle background images as follows:
- Front of postcard that conveys "CHANGE" of not just seasons - but of encouraging change of precinct voter representation - so anything about fall foliage / conveyance of change tie-in is worthy of considering
- Back of postcard - any Appalachian long rage mountain view that includes 5-7 layers of hills in the distance.
Some photos as samples to consider.

Target Market(s)

~2,700 registered Harvestliners and Unaffiliated voters

Requirements
Must have
• We require BOTH persuasive copy and high-impact layout for an oversized 6x11 political mailer. This might be one person, but it likely requires a specialized "creative team." of an experienced political strategist copywriter PLUS a graphic designer - so the words fit the exact layout block, and the visuals reinforce the psychological punch of the headline
Nice to have
• subtle background photos

```html
<!DOCTYPE html>
<html lang="en">
<head>
<meta charset="utf-8">
<title>New River III Precinct GOTV Postcard</title>
<link href="https://fonts.googleapis.com/css2?family=Oswald:wght@600;700&family=Roboto+Condensed:wght@400;500;700&display=swap" rel="stylesheet">
<style>
  :root {
    --backdrop: #9b9b9b;
    --paper: #ffffff;
    --panel: #f8f6f1;
    --headline-red: #c8191f;
    --navy: #1f2a78;
    --ink: #3a3a3a;
    --ink-dark: #1c1c1c;
    --rule: #8a8a8a;
    --leaf-dark: #7a3a1c;
    --leaf-red: #c8361d;
    --leaf-orange: #e5791f;
    --leaf-gold: #f2ac1e;
    --wood: #5a3a26;
    --sky-top: #e6e0ea;
    --sky-mid: #f2eeee;
    --ridge-far: #a9c0de;
    --ridge-near: #5d7fb3;
    --trees: #3e5a2e;
  }
  * { box-sizing: border-box; margin: 0; padding: 0; }
  html, body { width: 1200px; height: 904px; overflow: hidden; }
  body {
    background: var(--backdrop);
    font-family: "Roboto Condensed", "Arial Narrow", sans-serif;
    position: relative;
  }

  /* ---------- Front of postcard ---------- */
  .postcard-front {
    position: absolute; left: 97px; top: 58px;
    width: 700px; height: 381px; overflow: hidden;
  }
  .foliage-frame {
    position: absolute; inset: 0;
    background:
      radial-gradient(circle at 8% 12%, var(--leaf-red) 0 9%, transparent 16%),
      radial-gradient(circle at 50% 4%, var(--leaf-orange) 0 6%, transparent 12%),
      radial-gradient(circle at 94% 18%, var(--leaf-red) 0 8%, transparent 15%),
      radial-gradient(circle at 4% 55%, var(--leaf-orange) 0 8%, transparent 14%),
      radial-gradient(circle at 97% 60%, var(--leaf-gold) 0 8%, transparent 14%),
      radial-gradient(circle at 15% 96%, var(--leaf-red) 0 9%, transparent 16%),
      radial-gradient(circle at 60% 98%, var(--leaf-gold) 0 8%, transparent 14%),
      radial-gradient(circle at 90% 95%, var(--leaf-orange) 0 9%, transparent 16%),
      linear-gradient(135deg, var(--leaf-dark), var(--wood) 45%, var(--leaf-dark));
  }
  .message-panel {
    position: absolute; left: 52px; top: 52px;
    width: 597px; height: 278px;
    background: var(--panel);
  }
  .headline {
    position: absolute; left: 0; right: 0; top: 17px;
    text-align: center;
    font-family: "Oswald", "Arial Narrow", sans-serif;
    font-weight: 700; font-size: 22px; letter-spacing: 0.2px;
    color: var(--headline-red);
  }
  .issues {
    position: absolute; left: 32px; top: 51px; width: 318px;
    font-size: 7.4px; line-height: 10px; color: var(--ink);
  }
  .issues p { margin-bottom: 2.5px; }
  .issues p.spaced { margin-top: 4px; }
  .issue-label { color: var(--navy); font-weight: 500; }
  .column-rule {
    position: absolute; left: 370px; top: 54px;
    width: 1px; height: 205px; background: var(--rule);
  }
  .ballot {
    position: absolute; left: 389px; top: 51px; width: 200px;
    font-size: 7.6px; line-height: 10px;
  }
  .ballot-title { color: var(--headline-red); font-weight: 500; margin-bottom: 2.5px; }
  .ballot-item { margin-bottom: 4px; }
  .ballot-office { color: var(--ink-dark); }
  .ballot-candidate { color: var(--navy); font-weight: 500; }
  .ballot-candidate.plain { color: var(--ink-dark); }
  .ballot-measure { color: var(--headline-red); font-weight: 500; margin-bottom: 2.5px; }

  /* ---------- Back of postcard ---------- */
  .postcard-back {
    position: absolute; left: 377px; top: 474px;
    width: 700px; height: 381px; background: var(--paper);
  }
  .mountain-view {
    position: absolute; left: 10px; top: 10px;
    width: 423px; height: 360px;
    background: linear-gradient(180deg,
      var(--sky-top) 0%, var(--sky-mid) 40%, #dfe3ee 60%,
      var(--ridge-far) 68%, #8aa6d0 78%, var(--ridge-near) 86%, var(--trees) 100%);
  }
  .letter {
    position: absolute; left: 31px; top: 35px; width: 390px;
    font-size: 8.2px; line-height: 10.6px; color: var(--ink-dark);
  }
  .letter p { margin-bottom: 5px; }
  .letter p.tight { margin-top: -4px; }
  .greeting { color: var(--navy); font-weight: 500; margin-bottom: 0 !important; }
  .voter-facts {
    position: absolute; left: 31px; top: 165px;
    list-style: none;
    font-size: 8.2px; line-height: 12.4px;
    color: var(--navy); font-weight: 500;
  }
  .postage-indicia {
    position: absolute; left: 610px; top: 31px;
    width: 58px; height: 58px;
    border: 1px solid #b9b9b9;
    font-size: 7px; line-height: 9.5px; color: var(--ink-dark);
    text-align: center; padding-top: 5px;
  }
  .address-block {
    position: absolute; left: 465px; top: 128px;
    width: 204px; height: 53px;
    border: 1px solid #b9b9b9;
    font-size: 7.5px; line-height: 9.5px; color: var(--ink-dark);
    text-align: center; padding-top: 17px;
  }
</style>
</head>
<body>

<section class="postcard-front">
  <div class="foliage-frame" role="img" aria-label="Autumn leaves in red, orange and gold scattered on a dark wooden table"></div>
  <div class="message-panel">
    <h1 class="headline">VOTE FOR NEW REPRESENTATION</h1>

    <div class="issues">
      <p><span class="issue-label">LOCAL PAIN-THANKS TO CURRENT REPRESENTATIVES</span>-and sadly, to avoid accountability, they've cleverly delayed many/most impacts until AFTER the 2026 election, <span class="issue-label">VOTE FOR CHANGE</span></p>
      <p><span class="issue-label">FAMILY BUDGET:</span> exploded costs for everything, groceries, gas, car insurance, rent.</p>
      <p><span class="issue-label">HEALTH -</span> expired subsidies, tax credits mean "Im in NC will lose coverage or pay more. 50% cuts to Hospitals, Mental Health facilities, rural facilities will be closing</p>
      <p><span class="issue-label">REPRODUCTIVE RIGHTS -</span> Government authoritarian intrusion - censure women's rights.</p>
      <p><span class="issue-label">FOOD SECURITY -</span> Weaponized Hunger-cuts to SNAP; school meals cut, add'l work reqmts</p>
      <p><span class="issue-label">EDUCATION -</span> Watauga $2.2mm shortfall personnel cuts, freezes in hiring, teacher training. Abandoning civil rights of Special Ed students to HHS and DOL</p>
      <p><span class="issue-label">HOUSING -</span> 25% of renters are spending over 50% of income on rent. Especially bad locally, predatory leasing terms and skyrocketing rents. Proposed legislation is transforming HUD with the goal of getting rid of Section 8 housing that cares for vulnerable populations.</p>
      <p class="spaced"><span class="issue-label">ENERGY -</span> In 2022 Boone achieved 100% renewable energy in town buildings, this is now being destroyed by repeal of renewable energy project funding; Ridge State Innovation District prepares renewable workforce technologies-all this is now in limbo.</p>
      <p><span class="issue-label">ENVIRONMENT -</span> Reduced protections from coal ash pond leaks threaten public health. Corporations not held responsible for damage, public picks up the tab. Environmental Justice enforcement no longer a priority. Logging in Watauga with no public oversight. It's the "haz-mat" model do nothing, wait for catastrophe, then fix it.</p>
    </div>

    <div class="column-rule"></div>

    <div class="ballot">
      <p class="ballot-title">SAMPLE BALLOT RECOMMENDATIONS</p>
      <div class="ballot-item"><p class="ballot-office">US SENATE -</p><p class="ballot-candidate plain">RAY CALDER</p></div>
      <div class="ballot-item"><p class="ballot-office">US HOUSE-DISTRICT 5-</p><p class="ballot-candidate">CHET HALLOWAY</p></div>
      <p class="ballot-measure">REQMT TO SHOW ID FOR VOTERS NOT IN PERSON-NO</p>
      <div class="ballot-item"><p class="ballot-office">STATE SENATE DISTRICT 47-</p><p class="ballot-candidate">FRANK HOLLIS</p></div>
      <div class="ballot-item"><p class="ballot-office">HOUSE OF REP'S DISTRICT 93-</p><p class="ballot-candidate">CHARLIE WARREN</p></div>
      <div class="ballot-item"><p class="ballot-office">NC SUPREME COURT</p><p class="ballot-candidate">ANITA EBBERS</p></div>
      <div class="ballot-item"><p class="ballot-office">NC COURT OF APPEALS-SEAT 1</p><p class="ballot-candidate">JOHN ASHGROVE</p></div>
      <div class="ballot-item"><p class="ballot-office">NC COURT OF APPEALS-SEAT 2-</p><p class="ballot-candidate">TOBY HADLEY</p></div>
      <div class="ballot-item"><p class="ballot-office">NC COURT OF APPEALS-SEAT 3-</p><p class="ballot-candidate">CHRISTINE WOLCOTT</p></div>
    </div>
  </div>
</section>

<section class="postcard-back">
  <div class="mountain-view" role="img" aria-label="Hazy Appalachian long-range view with layered blue ridges and green treetops in the foreground"></div>

  <div class="letter">
    <p class="greeting">Dear New River III Neighbor.</p>
    <p>We live in a representative democracy. We expect our representatives will exercise independent thinking and support policies and legislation that don't harm us - and that reflect the MAJORITY VIEWS of precinct citizens.</p>
    <p>But our current representatives HAVE STOPPED LISTENING - they are now bringing harmful policies straight to Watauga County. IT'S TIME TO HOLD THEM ACCOUNTABLE AND VOTE THEM OUT.</p>
    <p class="tight">Make no mistake: in 2026, every election is partisan. Even Judicial seats are now tied directly to state platforms.</p>
    <p>Any candidate who refuses to publicly condemn Raleigh's gerrymandered overreach into Watauga politics-or refuses to fight funding cuts for our healthcare, education, and environmental justice - is actively supporting these harmful policies.</p>
    <p>They are hoping their silence fools you. DON'T BE FOOLED. This November, VOTE FOR CHANGE.</p>
  </div>

  <ul class="voter-facts">
    <li>YOU ARE A REGISTERED VOTER IN WATAUGA COUNTY</li>
    <li>YOU RESIDE IN PRECINCT: NEW RIVER III</li>
    <li>POLLING PLACES AVAILABLE TO YOU ARE: LOCATION,. 2, 3</li>
    <li>EARLY VOTING STARTS ON:</li>
    <li>DEADLINE TO APPLY FOR MAIL-IN BALLOTS</li>
    <li>KNOW THE RULES TO ENSURE YOUR MAIL-IN-BALLOT COUNTS</li>
  </ul>

  <div class="postage-indicia">PRSRT STD<br>ECRWSS<br>U.S. Postage<br>PAID<br>EDDM Retail</div>
  <div class="address-block">LOCAL POSTAL<br>CUSTOMER</div>
</section>

</body>
</html>
```